Velvet Harbor Boutique

The site is an Adult Retail Store website that sells products. There will be a Splash Page and inside (Home Page). The Splash page will have normal warning to users that 18+ material is inside. The splash page will contain....

- Lady (logo)
- disclaimer link for under 18
- enter and exit buttons
- Other detail in the must have

The client has also asked that this Splash Page must set the tone for the whole site and encourage users to enter. The client would like to give a feeling of romance, beauty, elegance, classy, inviting. The client would like to move away from the stigma associated with Adult stores as “sleezy” and create a welcoming feel for both males and females.

Also an internal Home Page will be created for the website which will take the same look and feel as the Splash Page. There will be a graphic header using some of the images below. Once the Home Page has been designer there will be minor colour background changes to the internal Home Page for the 2 Shop Pages (See Below).

Velvet Harbor is the largest adult store in Adelaide and will be using this website primarily to sell their products online.

Target Market(s)

Described as a “his and hers adult store” Velvet Harbor focuses on both males and females over the age of 18.

Requirements
Must have
• Velvet Harbors three main colours are Black, Purple and White. Please refer to current site for exact values.
• Also various gradients of these colours are encouraged to bring the website up to date with modern trends. The current website www.velvetharborboutique.com.au is very outdated!
• They would like the Lady larger and on the left of the Splash Page and an Enter Site on the Splash Page. They do not like the gothic font as such however they still want a softer gothic feel and appeal. The client quite likes the use of Trajan Pro font. I have attached a concept they quite liked to give an idea of the direction they would like to head in. This is by no means a suggested look and client is open to more suggestions. They would like to see some attention paid to modifying the lady to bring it up to date.
• The client has suggested a shining moon and some stars in the background of the Splash Page. Here the “under 18” content disclaimer link needs to be put discretely down the bottom of the Splash Page. The woman’s head will eventually be a Flash file which will have her hair flowing.
• When the visitor clicks through the Enter Site they will be shown the inside Home Page of the site with a similar feel to the Splash Page and contain typical menu links such as “about us” and “contact us”. On the Home Page there will be 2 doors “His” and “Hers” where the visitor will click through to the Shop. They like the idea of open doors to enter through. Both “His” and “Hers” shop pages will have the same theme as the Home Page with a minor change in the background. Possibly a darker colour for the males side and a lighter side for the females.
• The client has hand-picked the following images from pixmarrow.com. These may be used in the design of the Home Page at the designers discretion. Other similar images can be used to achieve the feel.
• (please search numbers at www.pixmarrow.com for thumbnails)
• #3920471
• #6053829
• #7146203
• #8271594
• #1538247
• #4682910
• If designer can also create the Flash component there will be an extra $300 paid. Please let us know.
Nice to have
• Whilst not part of the web design component here it will be of great use if designer had flash skills. This website requires some flash animation on the logo in the Splash Page and header of the Home Page that would require woman’s hair to flow so some ongoing work could be possible for winning designer.
Should not have
• Client has made the comment that they don’t want the site to be “boring and flat”

```html
<!DOCTYPE html>
<html lang="en">
<head>
<meta charset="utf-8">
<title>Velvet Harbor Boutique – His &amp; Hers Adult Shop</title>
<link href="https://fonts.googleapis.com/css2?family=Cinzel:wght@400;500&family=PT+Sans:wght@400;700&display=swap" rel="stylesheet">
<style>
:root{
  --black:#000;
  --bar:#050208;
  --purple-mid:#7a1fa8;
  --lilac:#d98cf0;
  --lilac-soft:#c9a3dc;
  --frame:#2a1a33;
  --tag-bg:#3a3a3a;
  --tag-border:#555;
  --white:#fff;
  --text:#e6e6e6;
  --grey-a:#9a9a9a;
  --grey-b:#c8c8c8;
}
*{box-sizing:border-box;margin:0;padding:0}
html,body{width:1200px;height:987px;overflow:hidden;background:var(--black)}
body{position:relative;font-family:"PT Sans",Tahoma,sans-serif;color:var(--text)}
a{text-decoration:none}
.top-bar{position:absolute;left:0;top:0;width:1200px;height:31px;background:var(--bar);border-top:1px solid var(--purple-mid);font-size:12.5px;color:var(--lilac)}
.top-bar .stores{position:absolute;left:144px;top:8px}
.top-bar .hours{position:absolute;right:140px;top:8px;word-spacing:1px}
.header{position:absolute;left:0;top:31px;width:1200px;height:283px;background:
  radial-gradient(ellipse 60px 60px at 718px 56px,#e9d8f2 0,#c7a5da 45%,rgba(150,70,190,0) 100%),
  radial-gradient(ellipse 700px 260px at 640px 60px,#8a2dc0 0,#5b1a86 45%,#2e0b48 80%),
  linear-gradient(180deg,#4a1470,#2a0a3e);}
.header .clouds{position:absolute;left:0;bottom:0;width:1200px;height:110px;background:linear-gradient(180deg,rgba(60,20,90,0),rgba(35,10,55,.85))}
.lady{position:absolute;left:178px;top:66px;width:216px;height:286px;border-radius:90px 90px 20px 20px;background:linear-gradient(180deg,#1a0624,#0a020f);z-index:3}
.brand{position:absolute;left:427px;top:84px;font-family:"Cinzel",serif;font-weight:400;font-size:56px;line-height:62px;color:#0a020f;letter-spacing:1px}
.tagline{position:absolute;left:428px;top:206px;font-family:"Cinzel",serif;font-weight:400;font-size:21px;color:var(--lilac-soft);letter-spacing:.5px}
.nav{position:absolute;left:500px;top:280px;display:flex;gap:7px;z-index:2}
.nav a{display:block;width:138px;height:34px;border-radius:9px 9px 0 0;background:linear-gradient(180deg,#6a1c9c,#4a0c74);border:1px solid #8a3cbc;border-bottom:none;color:var(--white);text-align:center;font-family:"Cinzel",serif;font-size:18px;line-height:36px}
.band{position:absolute;left:0;top:314px;width:1200px;height:39px;background:linear-gradient(180deg,#3a0d58,#1e0830);border-top:1px solid #6a2a98}
.content-frame{position:absolute;left:131px;top:354px;width:937px;height:563px;background:var(--frame)}
.content{position:absolute;left:12px;top:12px;width:913px;height:539px;background:var(--black)}
.welcome{position:absolute;left:25px;top:27px;font-size:14.5px;font-weight:700;color:var(--lilac);letter-spacing:.2px}
.intro{position:absolute;left:25px;top:62px;width:575px;font-size:12.5px;line-height:17px;color:var(--text)}
.intro p+p{margin-top:17px}
.tags{position:absolute;left:26px;top:144px;width:600px;list-style:none;display:flex;flex-wrap:wrap;column-gap:5px;row-gap:5px}
.tags li{height:19px;padding:0 10px 0 4px;background:var(--tag-bg);border:1px solid var(--tag-border);font-size:12.5px;line-height:17px;color:var(--text);display:flex;align-items:center;gap:6px}
.tags li::before{content:"";width:11px;height:11px;border-radius:50%;background:radial-gradient(circle at 40% 40%,#d9a8f0,#8a3cbc)}
.tags .br{flex-basis:100%;height:0;padding:0;border:none;background:none}
.tags .br::before{display:none}
.closing{position:absolute;left:27px;top:264px;width:575px;font-size:12.5px;line-height:17px}
.couple{position:absolute;left:640px;top:4px;width:244px;height:310px;border-radius:40% 10% 10% 40%;background:radial-gradient(ellipse at 60% 45%,#b9a3c4 0,#6e5680 40%,#2a1a33 75%,#000 100%)}
.door{position:absolute;top:384px;width:292px;height:122px;border-radius:8px;background:#3a3a3a;display:flex}
.door.his{left:122px}
.door.hers{left:454px}
.door .panel{position:relative;margin:7px 0 7px 7px;width:214px;height:108px;border-radius:5px 0 0 5px;overflow:hidden}
.door.his .panel{background:linear-gradient(90deg,#4a2a20 0,#8a5a3e 22%,#6a1590 25%,#7a1aa2 100%)}
.door.hers .panel{background:linear-gradient(90deg,#2a1a1a 0,#6a4a40 22%,#b04ad0 25%,#c85ae0 100%)}
.door .open{position:absolute;right:10px;top:8px;font-size:14.5px;color:var(--white);display:flex;align-items:center;gap:6px}
.door .label{flex:1;border-radius:0 8px 8px 0;background:linear-gradient(180deg,var(--grey-b),var(--grey-a) 50%,var(--grey-b));border-left:2px solid #777;font-family:"Cinzel",serif;font-size:23px;color:var(--white);text-decoration:none;display:flex;align-items:center;justify-content:center;text-shadow:0 1px 1px #666}
</style>
</head>
<body>
<div class="top-bar">
  <span class="stores">Stores at Marrowdale &amp; Fernbrook Park</span>
  <span class="hours">Mon - Sat : 10.30 am - Late&nbsp; Sunday : 12.00 noon - Late</span>
</div>

<header class="header" role="img" aria-label="Night sky with full moon over purple clouds">
  <div class="clouds"></div>
</header>
<div class="lady" role="img" aria-label="Silhouette of a woman holding a sword"></div>
<div class="brand">VELVET HARBOR<br>BOUTIQUE</div>
<div class="tagline">HIS &amp; HERS ADULT SHOP</div>
<nav class="nav">
  <a href="#">HOME</a><a href="#">ABOUT US</a><a href="#">OUR SHOPS</a><a href="#">CONTACT US</a>
</nav>
<div class="band"></div>

<main class="content-frame">
  <section class="content">
    <h1 class="welcome">Welcome to our business - Velvet Harbor Boutique His &amp; Hers Adult Shop</h1>
    <div class="intro">
      <p>Velvet Harbor Boutique was established in 1985 at Fernbrook Park and established at Marrowdale in 2003.</p>
      <p>We have worked very hard to make our adult shops the one stop adult shop by keeping the biggest selection of adult products:</p>
    </div>
    <ul class="tags">
      <li>Toys for women and men</li><li>Lingerie</li><li>Education DVDs, videos, books</li><li class="br"></li>
      <li>Shoes</li><li>Contact mags</li><li>Leather</li><li>Magazines (softcore &amp; hardcore)</li><li class="br"></li>
      <li>Bondage</li><li>Novels</li><li>Lubes, lotions, massage oils &amp; sprays</li><li>Condoms</li><li class="br"></li>
      <li>Adult games</li><li>Pills for men &amp; women</li><li>Body jewellery</li><li>Latex for men &amp; women</li>
    </ul>
    <p class="closing">We have a large range of DVDs, videos and novelties for all occasions so don't hesitate to come in and see us or call our friendly staff for more information.</p>
    <div class="couple" role="img" aria-label="Romantic photo of an embracing couple with purple swirl ornament"></div>

    <a class="door his" href="#">
      <div class="panel" role="img" aria-label="Men's torso photo with purple swirl">
        <span class="open">Click to Open <svg width="13" height="14" viewBox="0 0 13 14"><path d="M1.5 1.5 L11.5 7 L1.5 12.5 Z" fill="none" stroke="#fff" stroke-width="2"/></svg></span>
      </div>
      <span class="label">HIS</span>
    </a>
    <a class="door hers" href="#">
      <div class="panel" role="img" aria-label="Women's lingerie photo with purple swirl">
        <span class="open">Click to Open <svg width="13" height="14" viewBox="0 0 13 14"><path d="M1.5 1.5 L11.5 7 L1.5 12.5 Z" fill="none" stroke="#fff" stroke-width="2"/></svg></span>
      </div>
      <span class="label">HERS</span>
    </a>
  </section>
</main>
</body>
</html>
```